Rack Card for Portuguese Walking Food Tour

I would like a vertical rack card measuring 99x210mm. Here is the information I would like to include. It does not need to be in this format. We are located in Setubal, Portugal.
Please use the attached Teal Heron Logo.
Setúbal: Tradition and Today
Experience the culinary delights of Setúbal, Portugal with a walking food tour around our waterfront village. Discover the Mercado da Gaivota Branca, voted one of the world’s best markets by Metro Ledger, and indulge in local wines and dishes. Prepare for a calm stroll on flat streets. No hills to climb on this tour.
Duration: 4 hours
www.brinebasketwalks.com
+351 265 000 487

```html
<!DOCTYPE html>
<html lang="en">
<head>
<meta charset="utf-8">
<title>Brine Basket Walks – Setúbal Rack Card</title>
<link rel="stylesheet" href="https://fonts.googleapis.com/css2?family=Montserrat:wght@400;500;600;700;800&display=swap">
<style>
  :root {
    --backdrop: #6d6e72;
    --paper: #ffffff;
    --brand-orange: #f26522;
    --slate: #66676c;
    --body-grey: #6a6b70;
    --ink: #1f1f22;
  }
  html, body {
    margin: 0;
    width: 1200px;
    height: 1186px;
    overflow: hidden;
    background: var(--backdrop);
    font-family: "Montserrat", sans-serif;
  }
  .rack-card {
    position: absolute;
    left: 340px;
    top: 42px;
    width: 585px;
    height: 1240px;
    transform: scale(0.8889);
    transform-origin: top left;
    background: var(--paper);
    overflow: hidden;
    box-shadow: 0 8px 24px rgba(0,0,0,0.35);
  }
  .card-shapes {
    position: absolute;
    inset: 0;
    width: 585px;
    height: 1240px;
  }
  .brand {
    position: absolute;
    top: 92px;
    left: 0;
    width: 585px;
    display: flex;
    align-items: center;
    justify-content: center;
    gap: 22px;
  }
  .brand-dot {
    width: 86px;
    height: 86px;
    border-radius: 50%;
    background: var(--brand-orange);
    flex: none;
  }
  .brand-name {
    font-weight: 700;
    font-size: 38px;
    line-height: 1.08;
    color: var(--slate);
    margin: 0;
  }
  .tour-title {
    position: absolute;
    top: 722px;
    left: 0;
    width: 585px;
    margin: 0;
    text-align: center;
    font-weight: 700;
    font-size: 48px;
    line-height: 60px;
    color: var(--brand-orange);
  }
  .tour-tagline {
    position: absolute;
    top: 780px;
    left: 0;
    width: 585px;
    margin: 0;
    text-align: center;
    font-weight: 500;
    font-size: 21px;
    letter-spacing: 5px;
    color: var(--ink);
  }
  .tour-description {
    position: absolute;
    top: 827px;
    left: 0;
    width: 585px;
    margin: 0;
    text-align: center;
    font-weight: 400;
    font-size: 21.5px;
    line-height: 26.2px;
    color: var(--body-grey);
  }
  .duration-pill {
    position: absolute;
    top: 1060px;
    left: 152px;
    width: 262px;
    height: 38px;
    border-radius: 6px;
    border: 2px solid var(--paper);
    box-sizing: border-box;
    background: var(--slate);
    color: var(--paper);
    font-weight: 600;
    font-size: 24px;
    line-height: 34px;
    text-align: center;
  }
  .contact-phone {
    position: absolute;
    top: 1118px;
    left: 0;
    width: 585px;
    margin: 0;
    text-align: center;
    font-weight: 800;
    font-size: 50px;
    line-height: 60px;
    color: var(--paper);
  }
  .contact-web {
    position: absolute;
    top: 1180px;
    left: 0;
    width: 585px;
    margin: 0;
    text-align: center;
    font-weight: 500;
    font-size: 26px;
    line-height: 32px;
    color: var(--paper);
  }
</style>
</head>
<body>
  <article class="rack-card">
    <svg class="card-shapes" viewBox="0 0 585 1240" aria-hidden="false">
      <defs>
        <linearGradient id="market-tones" x1="0" y1="0" x2="1" y2="1">
          <stop offset="0" stop-color="#7fbcbc"/>
          <stop offset="0.25" stop-color="#d9624a"/>
          <stop offset="0.55" stop-color="#eaa488"/>
          <stop offset="0.8" stop-color="#c9493a"/>
          <stop offset="1" stop-color="#9aa3a6"/>
        </linearGradient>
      </defs>
      <rect class="market-photo" x="0" y="200" width="585" height="580" fill="url(#market-tones)" role="img" aria-label="Photo of fresh red mullet on ice at the fish market"/>
      <path class="top-panel" d="M0,0 H585 V215 Q330,320 0,268 Z" fill="var(--paper)"/>
      <path class="top-swoosh" d="M0,268 Q330,320 585,215 V248 Q330,330 0,302 Z" fill="var(--slate)"/>
      <path class="top-rule" d="M0,302 Q330,330 585,248 V252 Q330,334 0,306 Z" fill="var(--paper)"/>
      <path class="bottom-swoosh" d="M0,748 Q250,648 585,664 V1240 H0 Z" fill="var(--slate)"/>
      <path class="bottom-panel" d="M0,780 Q290,686 585,700 V1240 H0 Z" fill="var(--paper)"/>
      <path class="contact-band" d="M0,1100 Q300,1052 585,1102 V1240 H0 Z" fill="var(--brand-orange)"/>
    </svg>

    <header class="brand">
      <span class="brand-dot"></span>
      <p class="brand-name">Brine Basket<br>Walks</p>
    </header>

    <h1 class="tour-title">Setúbal</h1>
    <p class="tour-tagline">TRADITION &amp; TODAY</p>
    <p class="tour-description">Experience the culinary delights of<br>Setúbal, Portugal with a walking food tour<br>around our waterfront village. Discover the<br>Mercado da Gaivota Branca, voted one of the<br>world’s best markets by Metro Ledger, and<br>indulge in local wines and dishes. Prepare<br>for a calm stroll on flat streets. No hills to<br>climb on this tour.</p>

    <div class="duration-pill">Duration: 4 hours</div>

    <p class="contact-phone">+351 265 000 487</p>
    <p class="contact-web">www.brinebasketwalks.com</p>
  </article>
</body>
</html>
```